I teach courses in Lingo Drills in Crisis Care, paramedics, firefighters, nurses and all other Emergency related occupations. I need to let them know that this course is available and post this card on the bulletin boards of fire stations and other related offices. It has to call their attention.

Call

ec2027

• I would like a picture of a paramedic and a nurse. It can also have a firefighter as a second choice. Red is a good color to call attention. I am including a picture of me and a short bio to go on the reverse but this is not a must. I do not want my picture in the front.
I am thinking of an over sized postcard
• The title can be "Lingo Drills in Crisis Care" in full or "Lingo Drills CC's " depending on the fact that the whole name may be too long to make it stand out enough
• I do not know if my picture has come out in the right frame I see the cut is not right in the uploead. You might need to frame it right.

```html
<!DOCTYPE html>
<html lang="en">
<head>
<meta charset="utf-8">
<title>Lingo Drills in Crisis Care – Postcard</title>
<link href="https://fonts.googleapis.com/css2?family=PT+Sans+Narrow:wght@400;700&family=PT+Sans:wght@400;700&display=swap" rel="stylesheet">
<style>
  :root{
    --stage:#10293a;
    --paper:#ffffff;
    --ink:#111111;
    --night:#1f2433;
    --night-deep:#141826;
    --gold:#f5c400;
    --mist:#d6d9e0;
    --star:#f2a21a;
    --social:#3b5a9a;
    --warm:#f6b06a;
    --cool:#a9cfe8;
  }
  *{margin:0;padding:0;box-sizing:border-box}
  html,body{width:1200px;height:1000px;overflow:hidden;background:var(--stage)}
  body{position:relative;font-family:"PT Sans Narrow",sans-serif}

  .card{position:absolute;overflow:hidden}

  /* Promo side */
  .card--promo{left:461px;top:384px;width:674px;height:524px;
    background:linear-gradient(100deg,var(--night-deep) 0%,var(--night) 55%,#3a4150 100%);color:#fff}
  .promo__photo{position:absolute;right:0;top:0;width:420px;height:524px;
    background:
      linear-gradient(90deg,var(--night) 0%,rgba(31,36,51,.55) 35%,rgba(31,36,51,0) 60%),
      linear-gradient(180deg,#5b6a6e 0%,#3a4250 40%,#1a1d26 100%)}
  .promo__title{position:absolute;left:0;width:529px;top:34px;text-align:right;
    font-weight:700;font-style:italic;font-size:38px;color:var(--gold);white-space:nowrap}
  .promo__line{position:absolute;white-space:nowrap;text-align:right}
  .promo__lead{font-weight:700;font-size:18px;line-height:24px}
  .lead--1{right:243px;top:89px}
  .lead--2{right:272px;top:113px}
  .promo__point{font-size:14px;line-height:22px;color:var(--mist)}
  .point--1{right:280px;top:145px}
  .point--2{right:262px;top:167px}
  .promo__list{position:absolute;left:39px;top:211px;list-style:none;font-size:14px;line-height:22px;color:var(--mist)}
  .promo__list li::before{content:"•";margin-right:9px}
  .promo__list .faint{opacity:.45}
  .promo__sessions{position:absolute;left:39px;top:328px;font-weight:700;font-size:17px;line-height:25px}
  .promo__social{position:absolute;left:35px;top:410px;width:46px;height:46px;border-radius:50%;background:var(--social)}
  .promo__find{position:absolute;left:97px;top:404px;font-weight:700;font-size:17px;line-height:28px}
  .promo__call{position:absolute;left:36px;top:461px;font-weight:700;font-size:30px;color:var(--gold)}
  .promo__spot{position:absolute;width:100px;height:100px;border-radius:50%;border:2px solid #fff}
  .spot--fire{left:501px;top:236px;background:radial-gradient(circle,#f7a23a,#b8361a 60%,#2a1a14)}
  .spot--crew{left:512px;top:349px;background:radial-gradient(circle,#6e7c5a,#3f4a34 70%,#222)}
  .spot--hose{left:404px;top:393px;background:radial-gradient(circle,#f6b13c,#c2421c 60%,#3a1a10)}

  /* Bio side */
  .card--bio{left:85px;top:87px;width:675px;height:523px;
    background:
      radial-gradient(ellipse 60% 30% at 20% 48%,rgba(246,176,106,.55),transparent 70%),
      radial-gradient(ellipse 70% 35% at 80% 52%,rgba(169,207,232,.45),transparent 70%),
      linear-gradient(180deg,var(--paper) 0%,#fff7ef 55%,var(--paper) 100%);color:var(--ink)}
  .bio__portrait{position:absolute;left:41px;top:44px;width:120px;height:164px;border:2px solid #fff;
    background:linear-gradient(160deg,#8a5a3a,#c08a66 50%,#6b3f28)}
  .bio__name{position:absolute;left:180px;top:32px;font-weight:700;font-size:35px}
  .bio__creds{position:absolute;left:180px;top:76px;font-weight:700;font-size:19px}
  .bio__text{position:absolute;left:180px;top:102px;width:455px;font-size:16px;line-height:22.5px}
  .testimonial__label{position:absolute;left:39px;top:236px;font-weight:700;font-size:21px}
  .testimonial__quote{position:absolute;left:40px;top:283px;font-family:"PT Sans",sans-serif;font-size:27px;line-height:35px;white-space:nowrap}
  .testimonial__quote .open{font-family:Georgia,serif;font-weight:700;font-size:44px;vertical-align:-9px;margin-right:4px}
  .testimonial__quote .line2{display:block;padding-left:56px}
  .testimonial__close{position:absolute;left:543px;top:335px;font-family:Georgia,serif;font-size:42px;font-weight:700;color:#b9b9b9}
  .testimonial__stars{position:absolute;left:39px;top:378px}
  .testimonial__author{position:absolute;right:70px;top:383px;font-size:14px}
  .bio__social{position:absolute;left:35px;top:435px;width:60px;height:60px;border-radius:50%;background:var(--social)}
  .bio__find{position:absolute;left:106px;top:440px;font-size:14px}
  .bio__contact{position:absolute;left:106px;top:461px;font-weight:700;font-size:22px;white-space:nowrap}
  .bio__contact span{margin-left:22px}
</style>
</head>
<body>

<section class="card card--promo">
  <div class="promo__photo" role="img" aria-label="Photo of a smiling paramedic in uniform beside a patient on a stretcher"></div>
  <h1 class="promo__title">Lingo Drills in Crisis Care</h1>
  <p class="promo__line promo__lead lead--1">Spanish for nurses, paramedics, firefighters,</p>
  <p class="promo__line promo__lead lead--2">and all other emergency related occupations.</p>
  <p class="promo__line promo__point point--1">• Respond with confidence in any emergency situation</p>
  <p class="promo__line promo__point point--2">• Communicate clearly with your Spanish-speaking patients</p>
  <ul class="promo__list">
    <li class="faint">Meet new people while you practice</li>
    <li>Build a solid base for speaking Spanish in any situation sounding like a native</li>
    <li>Learn easily with " whole brain learning tools"</li>
    <li>Learn more about yourself and how you learn best</li>
    <li>Have great fun and de-stress</li>
  </ul>
  <p class="promo__sessions">Small groups and one-on-one coaching/tutoring sessions<br>available in Seaview, California.<br>For more information</p>
  <div class="promo__social" aria-hidden="true"></div>
  <p class="promo__find">find us on Linkspace<br>Marisol Everly or</p>
  <p class="promo__call">Call: 310 555 0142</p>
  <div class="promo__spot spot--fire" role="img" aria-label="Firefighter in gear facing flames"></div>
  <div class="promo__spot spot--crew" role="img" aria-label="Emergency responder outdoors"></div>
  <div class="promo__spot spot--hose" role="img" aria-label="Firefighters spraying a fire"></div>
</section>

<section class="card card--bio">
  <div class="bio__portrait" role="img" aria-label="Portrait photo of the instructor"></div>
  <h2 class="bio__name">Marisol Everly</h2>
  <p class="bio__creds">B.A., C.P.C.C.,</p>
  <p class="bio__text">brings to the classroom a superb blend of skills, knowledge and experience that allows her to design and teach unique courses in Spanish as a second language. Her native Spanish, "castellano "from Argentina, her many years of experience in linguistics and her studies in Life Coaching, Transformational Coaching and various other fields assures you a one of a kind language learning experience.</p>
  <h3 class="testimonial__label">Testimonial</h3>
  <p class="testimonial__quote"><span class="open">“</span>Learning Spanish with Marisol is easy and fun;<span class="line2">the language right on for my work!</span></p>
  <span class="testimonial__close" aria-hidden="true">”</span>
  <svg class="testimonial__stars" width="110" height="20" viewBox="0 0 110 20" aria-label="Five stars">
    <defs><polygon id="star" points="10,1 12.6,7 19,7.4 14,11.6 15.6,18 10,14.4 4.4,18 6,11.6 1,7.4 7.4,7" fill="var(--star)" stroke="#7a4a00" stroke-width="1"/></defs>
    <use href="#star" x="0"/><use href="#star" x="22"/><use href="#star" x="44"/><use href="#star" x="66"/><use href="#star" x="88"/>
  </svg>
  <p class="testimonial__author">- Tom R. Bayview</p>
  <div class="bio__social" aria-hidden="true"></div>
  <p class="bio__find">Find more on Linkspace</p>
  <p class="bio__contact">as Marisol Everly or<span>Call (310) 555 0142</span></p>
</section>

</body>
</html>
```